Food Hall in San Clemente, CA by the Pacific Ocean that has 15 vendors and 2 bars

We need a web page design that highlights our food hall in San Clemente, CA. The name of the food hall is Tidewell Food Hall. Inside of the food hall there are 15 different vendors and 2 bars. The place has a beautiful patio and it is by Pacific Ocean. Most of the vendors are local to San Clemente area. The highly anticipated location is opening during the summer of 2025. Website should have a dropdown menu for the different vendors that are in the food hall and people should be able to click to their respective business website. The website should also include link to our social media channels and also a link to provide comments and subscribe for the mailing list.
Target Market(s)
Mostly residents in the San Clemente, CA and surrounding areas. Couples, families and tourist alike that are looking for an exceptional dining experience that everyone can find something they like.
Industry/Entity Type
Restaurants
Coding
Coded - Design and coding required
Number of Pages Required
5+ page
Font styles to use
Look and feel
Each slider illustrates characteristics of the customer's brand and the style your logo design should communicate.

```html
<!DOCTYPE html>
<html lang="en">
<head>
<meta charset="utf-8">
<title>Tidewell Food Hall – San Clemente</title>
<link href="https://fonts.googleapis.com/css2?family=Montserrat:ital,wght@0,400;0,500;0,600;0,700;1,400&display=swap" rel="stylesheet">
<style>
:root{
  --ink:#111111;
  --muted:#555555;
  --soft:#9a9a9a;
  --white:#ffffff;
  --blue:#0a4fae;
  --blue-light:#c9d9ee;
  --line:#e2e2e2;
  --star:#f5a623;
  --hero-a:#4a3e33;
  --hero-b:#2c2620;
}
*{box-sizing:border-box;margin:0;padding:0}
html,body{width:1200px;height:3958px;overflow:hidden}
body{position:relative;font-family:'Montserrat',sans-serif;color:var(--ink);background:var(--white)}
.abs{position:absolute}
a{color:inherit;text-decoration:none}
h1,h2,h3,h4{font-weight:500}

/* hero */
.hero{position:absolute;left:0;top:0;width:1200px;height:728px;background:linear-gradient(160deg,#6b5c4b 0%,var(--hero-a) 40%,#3d4a2e 70%,var(--hero-b) 100%)}
.nav{position:absolute;top:0;left:0;width:1200px;height:82px;z-index:2;color:var(--white)}
.nav-links{position:absolute;left:57px;top:32px;display:flex;gap:41px;font-size:15px}
.logo{position:absolute;left:0;width:1260px;top:24px;text-align:center;font-size:31px;font-weight:500;color:var(--white);white-space:nowrap}
.btn-contact{position:absolute;left:1005px;top:21px;width:134px;height:40px;background:var(--white);color:var(--ink);border-radius:4px;font-size:14px;font-weight:600;display:flex;align-items:center;justify-content:center}
.hero-content{position:absolute;z-index:2;color:var(--white)}
.kicker{left:60px;top:248px;font-size:26px;font-weight:400}
.hero-title{left:60px;top:292px;font-size:70px;font-weight:600;line-height:82px}
.reviews{left:72px;top:578px}
.avatars{position:absolute;left:0;top:0;display:flex}
.avatars span{width:40px;height:40px;border-radius:50%;border:2px solid var(--white);background:linear-gradient(#c8b6a0,#7d6a58);margin-right:-14px}
.stars{position:absolute;left:120px;top:-2px;color:var(--star);font-size:20px;letter-spacing:4px;white-space:nowrap}
.rev-count{position:absolute;left:118px;top:26px;font-size:14px;white-space:nowrap}
.hero-note{left:60px;top:637px;font-size:11px;line-height:18px;width:250px}
.hero-side{left:793px;top:600px;font-size:16px;line-height:24px;width:350px}
.down{position:absolute;left:572px;top:700px;width:56px;height:56px;border-radius:50%;background:var(--white);box-shadow:0 2px 8px rgba(0,0,0,.25);z-index:3;display:flex;align-items:center;justify-content:center}

/* vendors */
.h2{font-size:49px;font-weight:500;line-height:52px}
.vendors-title{left:60px;top:838px}
.btn-blue{position:absolute;background:var(--blue);color:var(--white);font-weight:600;display:flex;align-items:center;justify-content:center;border-radius:3px}
.vendors-btn{left:963px;top:891px;width:177px;height:49px;font-size:19px}
.card{position:absolute;top:986px;width:346px;height:432px;border-radius:14px;border:2px solid var(--line);overflow:hidden;background:var(--white)}
.card-img{position:absolute;left:0;top:0;width:100%;height:252px}
.card-body{position:absolute;left:13px;top:262px;right:13px}
.card-name{font-size:23px;font-weight:600;margin-bottom:14px}
.card-text{font-size:15px;line-height:24px;color:#333}
.card-link{font-size:18px;font-weight:700;margin-top:20px}
.card-full .card-img{height:100%}
.card-full .card-name{position:absolute;left:22px;bottom:26px;color:var(--white);font-size:31px;font-weight:500;margin:0}
.track{left:60px;top:1452px;width:1080px;height:3px;background:#8a8a8a}
.thumb{left:166px;top:1445px;width:160px;height:16px;border-radius:8px;background:var(--ink)}

/* patio band */
.patio{left:0;top:1570px;width:1200px;height:396px;background:linear-gradient(135deg,#4b4f48,#2d312c 55%,#3b3a33)}
.patio-title{left:0;top:1667px;width:1200px;text-align:center;color:var(--white);font-size:49px;font-weight:400;line-height:63px}
.patio-btn{left:522px;top:1822px;width:155px;height:46px;font-size:18px;font-weight:400}

/* bars */
.pour-title{left:0;top:2078px;width:1200px;text-align:center}
.beer-img{left:61px;top:2241px;width:437px;height:488px;border-radius:10px;background:radial-gradient(circle at 55% 45%,#d08a2e,#8a4a14 45%,#2a1e14 80%)}
.drink{position:absolute;width:278px;height:165px;border-radius:14px;border:2px solid var(--line);background:var(--white);padding:28px 16px}
.drink.active{background:var(--blue-light);border-color:#bccde6}
.drink h3{font-size:24px;font-weight:500;margin-bottom:10px}
.drink p{font-size:15px;line-height:22px;font-style:italic;color:var(--soft)}
.pour-btn{left:541px;top:2665px;width:178px;height:49px;font-size:19px}

/* contact */
.contact-title{left:0;top:2842px;width:1200px;text-align:center}
.map{left:108px;top:2954px;width:428px;height:445px;border-radius:14px;background:linear-gradient(150deg,#efe6cf,#e4dcc4 50%,#c7dba8)}
.field{position:absolute;border:2px solid #9a9a9a;border-radius:4px;font-size:15px;padding:10px 20px;color:var(--ink)}
.submit{left:567px;top:3355px;width:525px;height:43px;font-size:16px}

/* footer */
.footer{left:0;top:3513px;width:1200px;height:445px;background:linear-gradient(160deg,#2b302b,#1a1d1b 60%,#262a25)}
.f-logo{left:60px;top:3639px;font-size:35px;font-weight:500;color:var(--white);white-space:nowrap}
.f-sub{left:60px;top:3720px;font-size:17px;color:#dcdcdc}
.f-input{left:60px;top:3759px;width:258px;height:44px;border:1.5px solid var(--white);border-radius:4px;background:var(--white)}
.f-input span{position:absolute;left:12px;top:14px;font-size:13px;color:var(--ink)}
.f-input i{position:absolute;right:0;top:0;width:48px;height:41px;border-left:1.5px solid #ccc;display:flex;align-items:center;justify-content:center}
.f-head{font-size:19px;font-weight:600;color:var(--white)}
.f-item{font-size:15px;color:#e4e4e4;display:flex;align-items:center;gap:12px;white-space:nowrap}
.f-link{font-size:15px;color:#e4e4e4}
.f-rule{left:60px;top:3894px;width:1080px;height:1px;background:#8c8c8c}
.copy{left:60px;top:3915px;font-size:11px;color:#dcdcdc}
.social{position:absolute;top:3907px;width:28px;height:28px;border-radius:50%;background:var(--white)}
</style>
</head>
<body>

<!-- hero -->
<section class="hero" role="img" aria-label="Interior of a modern food hall with wooden ceiling, long tables and green benches"></section>
<header class="nav">
  <nav class="nav-links"><a>Home</a><a>Vendors</a><a>Bars</a><a>Patio</a></nav>
  <div class="logo">Tidewell Food Hall</div>
  <a class="btn-contact">Contact now!</a>
</header>
<p class="abs hero-content kicker">Coming Summer 2025</p>
<h1 class="abs hero-content hero-title">Where San Clemente<br>Eats Together</h1>
<div class="abs hero-content reviews">
  <div class="avatars"><span></span><span></span><span></span><span></span></div>
  <div class="stars">★★★★★</div>
  <div class="rev-count">18,921 (reviews)</div>
</div>
<p class="abs hero-content hero-note">Saltline Provisions Is A US-Made Dietary Supplement Brand Focused On Advanced Formula Vitamins, Minerals</p>
<p class="abs hero-content hero-side">From Concept to Completion, We Create Architectural Masterpieces From Concept to Completion From</p>
<div class="down"><svg width="24" height="24" viewBox="0 0 24 24" fill="none" stroke="#111" stroke-width="2.2" stroke-linecap="round" stroke-linejoin="round"><path d="M12 4v15M5 12l7 7 7-7"/></svg></div>

<!-- vendors -->
<h2 class="abs h2 vendors-title">Explore 15 Unique Vendors – One<br>Delicious Destination</h2>
<a class="btn-blue vendors-btn">Discover More</a>

<article class="card card-full" style="left:61px">
  <div class="card-img" role="img" aria-label="Grilled plant-based steaks with char marks" style="background:radial-gradient(circle at 40% 40%,#7a5a3a,#3a2a1c 60%,#141210)"></div>
  <h3 class="card-name">Sunline Vegan Grill</h3>
</article>
<article class="card" style="left:425px">
  <div class="card-img" role="img" aria-label="Seafood rice dish with calamari and prawns" style="background:radial-gradient(circle at 50% 60%,#c0662e,#8e3d1e 50%,#e9d8c6 85%)"></div>
  <div class="card-body">
    <h3 class="card-name">Marea Mariscos</h3>
    <p class="card-text">From Concept To Completion,&nbsp; Create Architectural Masterpieces Fr Concept To Completion.</p>
    <p class="card-link">Learn More</p>
  </div>
</article>
<article class="card" style="left:791px">
  <div class="card-img" role="img" aria-label="Stacked burger with sesame bun, cheese and lettuce" style="background:radial-gradient(circle at 50% 45%,#c9853a,#6b3a1c 55%,#1e1a18 90%)"></div>
  <div class="card-body">
    <h3 class="card-name">The Harbor Patty</h3>
    <p class="card-text">From Concept To Completion,&nbsp; Create Architectural Masterpieces Fr Concept To Completion.</p>
    <p class="card-link">Learn More</p>
  </div>
</article>
<div class="abs track"></div>
<div class="abs thumb"></div>

<!-- patio -->
<section class="abs patio" role="img" aria-label="Outdoor patio with wooden tables and planters at dusk"></section>
<h2 class="abs patio-title">Soak Up The Sun, One Sip At A<br>Time Dine Outside.</h2>
<a class="btn-blue patio-btn">Discover More</a>

<!-- bars -->
<h2 class="abs h2 pour-title">Your Favorite Pour, Just<br>Steps From The Shore</h2>
<div class="abs beer-img" role="img" aria-label="Foaming mug of amber beer beside wheat stalks"></div>
<div class="drink active" style="left:541px;top:2256px"><h3>beer</h3><p>Enjoy a bespoke culinar journey with a multi-course tasting menu crafted by</p></div>
<div class="drink" style="left:541px;top:2467px"><h3>wine</h3><p>Enjoy a bespoke culinar journey with a multi-course tasting menu crafted by</p></div>
<div class="drink" style="left:862px;top:2339px"><h3>cocktails</h3><p>Enjoy a bespoke culinar journey with a multi-course tasting menu crafted by</p></div>
<div class="drink" style="left:862px;top:2550px"><h3>alcoholic drinks</h3><p>Enjoy a bespoke culinar journey with a multi-course tasting menu crafted by our</p></div>
<a class="btn-blue pour-btn">Discover More</a>

<!-- contact -->
<h2 class="abs h2 contact-title">Your Feedback Matters. Contact Us</h2>
<div class="abs map" role="img" aria-label="Street map showing the food hall location near the river"></div>
<div class="field" style="left:567px;top:2955px;width:247px;height:43px">Name</div>
<div class="field" style="left:845px;top:2955px;width:247px;height:43px">Phone</div>
<div class="field" style="left:567px;top:3029px;width:525px;height:45px">Email</div>
<div class="field" style="left:567px;top:3104px;width:525px;height:205px;padding-top:22px">Message</div>
<a class="btn-blue submit">Submit</a>

<!-- footer -->
<footer class="abs footer" role="img" aria-label="Evening patio with lounge chairs and greenery"></footer>
<div class="abs f-logo">Tidewell Food Hall</div>
<p class="abs f-sub">Subscribe News Letters</p>
<div class="abs f-input"><span>Your Email</span><i><svg width="14" height="14" viewBox="0 0 14 14" fill="none" stroke="#111" stroke-width="2" stroke-linecap="round"><path d="M5 2l5 5-5 5"/></svg></i></div>

<h4 class="abs f-head" style="left:501px;top:3660px">Contact Info</h4>
<p class="abs f-item" style="left:501px;top:3699px"><svg width="17" height="17" viewBox="0 0 24 24" fill="none" stroke="#fff" stroke-width="2"><path d="M5 3h4l2 5-3 2a12 12 0 0 0 6 6l2-3 5 2v4a2 2 0 0 1-2 2A18 18 0 0 1 3 5a2 2 0 0 1 2-2z"/></svg>(949) 555-0147</p>
<p class="abs f-item" style="left:501px;top:3734px"><svg width="17" height="17" viewBox="0 0 24 24" fill="none" stroke="#fff" stroke-width="2"><rect x="3" y="5" width="18" height="14" rx="1"/><path d="M3 6l9 7 9-7"/></svg>info@ tidewellhall .example</p>
<p class="abs f-item" style="left:501px;top:3768px"><svg width="17" height="17" viewBox="0 0 24 24" fill="none" stroke="#fff" stroke-width="2"><circle cx="12" cy="12" r="9"/><path d="M12 7v5l3 2"/></svg>9AM To 5PM Monday - Friday</p>

<h4 class="abs f-head" style="left:883px;top:3660px">Quick Links</h4>
<a class="abs f-link" style="left:895px;top:3699px">Home</a>
<a class="abs f-link" style="left:895px;top:3735px">Vendors</a>
<a class="abs f-link" style="left:895px;top:3771px">Patio</a>

<h4 class="abs f-head" style="left:1060px;top:3660px">Bar</h4>
<a class="abs f-link" style="left:1060px;top:3702px">Wine</a>
<a class="abs f-link" style="left:1060px;top:3733px">Cocktails</a>
<a class="abs f-link" style="left:1060px;top:3764px">Beer</a>

<div class="abs f-rule"></div>
<p class="abs copy">Copyright 2025 . All Rights Reserved</p>
<span class="social" style="left:984px"></span>
<span class="social" style="left:1027px"></span>
<span class="social" style="left:1069px"></span>
<span class="social" style="left:1112px"></span>

</body>
</html>
```